Lumen Gathering 2019 Enemies of the End-Times Church Flyer

We want a church conference flyer designed. We are looking for a professional, yet catchy design that uses our brand colors and logo creatively while communicating key information of the event effectively. <br/>The flyer must include all of the following:<br/>Title: Lumen Gathering 2019<br/>Topic: The Enemies of The End-Times Church <br/>Subtitles: <br/> -How the antichrist raises an army by social behavior engineering. <br/>-How the architects of modern social constructs escaped the church's radar. <br/>-The Holy Spirit's end-times agenda:<br/> The Knock-Out Punch!<br/>Speaker: Prophet Marcus Obuya <br/>Dates/time: December 27, 28 & 29 at 6pm<br/>Location: Thistle Community Center <br/> 412 Farrow Lane <br/> Portland, ME 04219<br/>Contact info: phone: 207-583-1924 <br/>email: contact@vellorbrook.org <br/> www.toskin.org<br/>*The flyer must also include a picture of the speaker and our Toskin logo <br/>Thanks, we look forward to seeing what you come up with!

Colors

Designer to choose colors to be used in the design.

Requirements
Must have
• The flyer must include all of the following:
• Title: Lumen Gathering 2019
• Topic: The Enemies of The End-Times Church
• Subtitles:
• -How the antichrist raises an army by social behavior engineering.
• -How the architects of modern social constructs escaped the church's radar.
• -The Holy Spirit's end-times agenda:
• The Knock-Out Punch!
• Speaker: Prophet Marcus Obuya
• Dates/time: December 27, 28 & 29 at 6pm
• Location: Thistle Community Center
• 412 Farrow Lane
• Portland, ME 04219
• Contact info: phone: 207-583-1924
• email: contact@vellorbrook.org
• www.toskin.org
• *The flyer must also include a picture of the speaker and our Toskin logo
Should not have
• Pictures of crosses or church buildings

```html
<!DOCTYPE html>
<html lang="en">
<head>
<meta charset="utf-8">
<title>Lumen Gathering 2019 Flyer</title>
<link href="https://fonts.googleapis.com/css2?family=Anton&family=Oswald:wght@400;500;600&family=Roboto:wght@400&family=Tinos:wght@700&display=swap" rel="stylesheet">
<style>
  :root {
    --navy: #1f4d6d;
    --navy-deep: #173c57;
    --orange: #f7a12d;
    --orange-light: #fbbd5c;
    --white: #ffffff;
    --page: #e9e4e6;
  }
  * { margin: 0; padding: 0; box-sizing: border-box; }
  html, body { width: 1200px; height: 1037px; overflow: hidden; background: var(--page); }
  .flyer {
    position: absolute; left: 221px; top: 28px; width: 758px; height: 981px;
    background: var(--navy); overflow: hidden; color: var(--white);
    font-family: 'Oswald', sans-serif;
    box-shadow: 0 10px 30px rgba(0,0,0,.25);
  }
  .flame-shape { position: absolute; left: 0; top: 0; width: 758px; height: 981px; }
  .speaker-photo {
    position: absolute; left: 420px; top: 300px; width: 338px; height: 600px;
    background: linear-gradient(180deg, #3a3f48 0%, #2c3038 55%, #5a2030 100%);
    border-radius: 160px 0 0 0;
  }
  .title {
    position: absolute; left: 22px; top: 4px;
    font-family: 'Anton', sans-serif; font-size: 248px; line-height: 1;
    letter-spacing: 2px; color: var(--white);
  }
  .subtitle {
    position: absolute; left: 40px; top: 268px; display: flex; gap: 16px; align-items: baseline;
    font-family: 'Anton', sans-serif; font-size: 56px; line-height: 1;
  }
  .subtitle .word { color: var(--orange); }
  .subtitle .year { color: var(--white); }
  .subtitle-rule { position: absolute; left: 40px; top: 336px; width: 110px; height: 5px; background: var(--orange); }
  .topic {
    position: absolute; left: 50px; top: 366px; padding-left: 18px;
    border-left: 3px solid var(--orange);
    font-family: 'Oswald', sans-serif; font-weight: 600; font-size: 50px; line-height: 0.92;
    text-transform: uppercase;
  }
  .topic .accent { color: var(--orange); }
  .points {
    position: absolute; left: 62px; top: 580px; width: 285px; list-style: none;
    font-size: 15px; line-height: 1.35; font-weight: 400;
  }
  .points li { position: relative; padding-left: 12px; margin-bottom: 6px; }
  .points li::before { content: "•"; position: absolute; left: 0; color: var(--orange); }
  .points li.orange { color: var(--orange); }
  .burst { position: absolute; left: 360px; top: 560px; width: 190px; height: 190px; }
  .burst-text {
    position: absolute; left: 390px; top: 614px; width: 130px; text-align: center;
    transform: rotate(-14deg);
    font-family: 'Anton', sans-serif; font-size: 23px; line-height: 1.05; color: var(--navy);
  }
  .burst-text .mid { color: var(--orange); }
  .date-pill {
    position: absolute; left: 78px; top: 716px; width: 220px; height: 66px;
    border-radius: 33px; background: linear-gradient(180deg, var(--orange-light), var(--orange));
    text-align: center; font-weight: 500; font-size: 22px; line-height: 1.35; padding-top: 2px;
  }
  .date-pill .at { color: var(--navy); }
  .pin { position: absolute; left: 177px; top: 794px; width: 20px; height: 27px; }
  .venue {
    position: absolute; left: 70px; top: 834px; width: 240px; text-align: center;
    border: 1px solid var(--white); border-top: none; padding: 0 4px 3px;
  }
  .venue-name { display: block; margin-top: -12px; background: var(--navy); padding: 0 6px; font-size: 20px; color: var(--orange); line-height: 1.2; width: fit-content; margin-left: auto; margin-right: auto; }
  .venue-address { font-family: 'Roboto', sans-serif; font-size: 12px; }
  .brand { position: absolute; left: 62px; top: 870px; display: flex; align-items: center; gap: 8px; }
  .brand-dot { width: 14px; height: 14px; border-radius: 50%; background: var(--orange); }
  .brand-name { font-family: 'Oswald', sans-serif; font-weight: 400; font-size: 30px; line-height: 1; letter-spacing: 1px; color: var(--white); }
  .contact { position: absolute; left: 62px; top: 908px; font-family: 'Roboto', sans-serif; }
  .phone { display: flex; align-items: center; gap: 6px; font-family: 'Oswald', sans-serif; font-weight: 500; font-size: 30px; line-height: 1; }
  .contact-line { display: flex; align-items: center; gap: 8px; font-size: 13px; line-height: 1.2; margin-top: 3px; }
  .contact-line .hl { color: var(--orange); }
  .icon { width: 13px; height: 13px; flex: none; }
  .phone .icon { width: 20px; height: 20px; }
  .speaker-band {
    position: absolute; left: 420px; top: 810px; width: 338px; height: 74px;
    background: linear-gradient(90deg, rgba(247,161,45,0) 0%, rgba(247,161,45,.55) 45%, var(--orange) 100%);
    font-family: 'Tinos', serif; font-weight: 700; padding: 8px 0 0 34px; line-height: 1.1;
  }
  .speaker-label { color: var(--orange); font-size: 24px; }
  .speaker-name { color: var(--white); font-size: 27px; }
</style>
</head>
<body>
<main class="flyer">
  <svg class="flame-shape" viewBox="0 0 758 981" aria-hidden="true">
    <path d="M500 95 C600 110 700 130 758 170 L758 981 L470 981 C400 880 360 760 410 640 C440 560 480 520 470 440 C560 500 600 420 560 330 C540 260 510 180 500 95 Z" fill="var(--orange)"/>
    <path d="M600 220 C680 300 720 420 700 560 L640 600 C660 480 640 340 600 220 Z" fill="var(--navy)"/>
  </svg>

  <div class="speaker-photo" role="img" aria-label="Portrait photo of the speaker, Prophet Marcus Obuya, in a dark blazer and red sweater"></div>

  <h1 class="title">LUMEN</h1>
  <div class="subtitle"><span class="word">GATHERING</span><span class="year">2019</span></div>
  <div class="subtitle-rule"></div>

  <h2 class="topic">The Enemies<br>of the<br><span class="accent">End-Times<br>Church</span></h2>

  <ul class="points">
    <li>How the antichrist raises an army by social behavior engineering.</li>
    <li class="orange">How the architects of modern social constructs escaped the church's radar.</li>
    <li>The Holy Spirit's end-times agenda:</li>
  </ul>

  <svg class="burst" viewBox="0 0 200 200" aria-hidden="true">
    <polygon fill="var(--white)" points="100,0 118,58 170,20 140,74 200,80 146,104 190,150 128,128 130,196 100,140 70,196 72,128 10,150 54,104 0,80 60,74 30,20 82,58"/>
  </svg>
  <div class="burst-text">The<br><span class="mid">Knock-Out</span><br>Punch !</div>

  <div class="date-pill">December<br>27, 28 &amp; 29 <span class="at">at</span> 6pm</div>

  <svg class="pin" viewBox="0 0 22 30" aria-hidden="true">
    <path d="M11 0 C4.9 0 0 4.9 0 11 C0 19 11 30 11 30 C11 30 22 19 22 11 C22 4.9 17.1 0 11 0 Z M11 15.5 A4.5 4.5 0 1 1 11 6.5 A4.5 4.5 0 1 1 11 15.5 Z" fill="var(--orange)"/>
  </svg>
  <div class="venue">
    <span class="venue-name">Thistle Community Center</span>
    <div class="venue-address">412 Farrow Lane Portland, ME 04219</div>
  </div>

  <div class="brand"><span class="brand-dot"></span><span class="brand-name">TOSKIN</span></div>

  <div class="contact">
    <div class="phone">
      <svg class="icon" viewBox="0 0 20 20" aria-hidden="true"><circle cx="10" cy="10" r="9" fill="none" stroke="var(--white)" stroke-width="1.5"/><path d="M6.5 5.5 L8.5 5.5 L9.3 8 L8 9 C8.7 10.5 9.6 11.4 11 12 L12 10.7 L14.5 11.5 L14.5 13.5 C10 14 6 10 6.5 5.5 Z" fill="var(--orange)"/></svg>
      207-583-1924
    </div>
    <div class="contact-line">
      <svg class="icon" viewBox="0 0 14 14" aria-hidden="true"><circle cx="7" cy="7" r="6.3" fill="none" stroke="var(--orange)" stroke-width="1.2"/><rect x="3.5" y="4.5" width="7" height="5" fill="none" stroke="var(--white)" stroke-width="1"/><path d="M3.5 4.5 L7 7.5 L10.5 4.5" fill="none" stroke="var(--white)" stroke-width="1"/></svg>
      <span>contact@vellorbrook.org</span>
    </div>
    <div class="contact-line">
      <svg class="icon" viewBox="0 0 14 14" aria-hidden="true"><circle cx="7" cy="7" r="6.3" fill="none" stroke="var(--orange)" stroke-width="1.2"/><circle cx="7" cy="7" r="3.5" fill="none" stroke="var(--white)" stroke-width="1"/><path d="M3.5 7 H10.5 M7 3.5 V10.5" stroke="var(--white)" stroke-width="1"/></svg>
      <span>www.<span class="hl">toskin</span>.org</span>
    </div>
  </div>

  <div class="speaker-band">
    <div class="speaker-label">Speaker:</div>
    <div class="speaker-name">Prophet Marcus Obuya</div>
  </div>
</main>
</body>
</html>
```